Postcard design to acquire new clients for my Property Management Company

I'm looking for a postcard design that I can send to prospective clients detailing information about my company and services.
Postcard should be eye catching and contain information from www.brightkeyrentals-example.com. I've provided a few screen shots for the most important information and my logo.
Target Market(s)
Real Estate
Industry/Entity Type
Real Estate
Font styles to use
Sans Serif
Requirements
Must have
- Must be eye catching!! this will be a direct mail piece - I'd like for the card to be read and not tossed in the trash immediately.
Design que from the logo.
A place to write / print the receipts name and address.
our physical address - 2287 Marble Lane, Lubbock, TX 79555.
Should not have
- the contact information on the business card is not accurate - please use info from website.

```html
<!DOCTYPE html>
<html lang="en">
<head>
<meta charset="utf-8">
<title>BrightKey Property Management – Postcard</title>
<link rel="stylesheet" href="https://fonts.googleapis.com/css2?family=Montserrat:wght@400;500;600;700;800;900&display=swap">
<style>
  :root {
    --stage: #414143;
    --navy: #0b4a8b;
    --navy-deep: #0a3f7a;
    --check: #2aa6e0;
    --white: #ffffff;
  }
  * { box-sizing: border-box; margin: 0; padding: 0; }
  html, body { width: 1044px; height: 1200px; overflow: hidden; }
  body {
    background: var(--stage);
    font-family: "Montserrat", sans-serif;
    color: var(--navy);
    position: relative;
  }
  .postcard {
    position: absolute;
    left: 174px;
    width: 695px;
    height: 463px;
    overflow: hidden;
  }
  .postcard--front { top: 129px; }
  .postcard--back { top: 609px; background: var(--white); }

  /* Front */
  .front-art { position: absolute; inset: 0; width: 695px; height: 463px; }
  .headline {
    position: absolute; left: 47px; top: 44px;
    font-size: 29px; line-height: 31px;
    font-weight: 400; letter-spacing: 0.2px;
  }
  .headline strong { font-weight: 800; }
  .brand {
    position: absolute;
    color: var(--navy);
    text-transform: uppercase;
    line-height: 1;
    white-space: nowrap;
  }
  .brand__name { display: block; font-weight: 700; }
  .brand__tag { display: block; font-weight: 500; }
  .brand--front { left: 465px; top: 33px; }
  .brand--front .brand__name { font-size: 24px; letter-spacing: 5.4px; }
  .brand--front .brand__tag { font-size: 10.5px; letter-spacing: 2.3px; margin-top: 4px; }
  .front-rule {
    position: absolute; left: 480px; right: 0; top: 84px;
    height: 1.5px; background: var(--navy);
  }
  .front-contact {
    position: absolute; left: 498px; top: 93px;
    list-style: none; font-size: 9.6px; font-weight: 500; line-height: 14px;
    white-space: nowrap;
  }
  .front-contact li { display: flex; align-items: center; gap: 4px; }
  .icon { width: 8px; height: 8px; fill: var(--navy); flex: none; }

  /* Back */
  .back-art { position: absolute; inset: 0; width: 695px; height: 463px; }
  .brand--back { left: 463px; top: 17px; }
  .brand--back .brand__name { font-size: 20px; letter-spacing: 4.4px; }
  .brand--back .brand__tag { font-size: 8.6px; letter-spacing: 1.9px; margin-top: 3px; }
  .brand__address {
    display: block; margin-top: 5px;
    font-size: 8.6px; font-weight: 500; letter-spacing: 0.2px; text-transform: none;
  }
  .services {
    position: absolute; left: 52px; top: 90px;
    width: 318px; height: 329px;
    background: rgba(255,255,255,0.88);
    border-radius: 24px;
  }
  .services__title {
    position: absolute; left: 0; right: 0; top: 13px;
    text-align: center; font-weight: 800;
    font-size: 29px; line-height: 27px; letter-spacing: -0.3px;
  }
  .services__rule {
    position: absolute; left: 41px; width: 222px; top: 74px;
    height: 2px; background: var(--navy);
  }
  .services__list { position: absolute; left: 58px; top: 85px; list-style: none; }
  .services__list li {
    display: flex; align-items: center; gap: 6px;
    height: 29px; font-size: 17.5px; font-weight: 500;
  }
  .tick { width: 15px; height: 15px; flex: none; }
  .back-contact {
    position: absolute; left: 22px; top: 421px;
    display: flex; align-items: center; white-space: nowrap;
  }
  .back-contact__phone {
    display: flex; align-items: center; gap: 8px;
    font-size: 27px; font-weight: 800; letter-spacing: -0.3px;
  }
  .back-contact__phone .icon { width: 20px; height: 20px; }
  .back-contact__lines {
    list-style: none; margin-left: 9px;
    font-size: 9.6px; font-weight: 500; line-height: 12px;
  }
  .back-contact__lines li { display: flex; align-items: center; gap: 3px; }
  .back-contact__lines .icon { width: 7px; height: 7px; }
</style>
</head>
<body>

<svg width="0" height="0" style="position:absolute" aria-hidden="true">
  <defs>
    <symbol id="i-phone" viewBox="0 0 24 24"><path d="M6.6 10.8a15.1 15.1 0 0 0 6.6 6.6l2.2-2.2a1 1 0 0 1 1-.25 11.4 11.4 0 0 0 3.6.57 1 1 0 0 1 1 1V20a1 1 0 0 1-1 1A17 17 0 0 1 3 4a1 1 0 0 1 1-1h3.5a1 1 0 0 1 1 1c0 1.25.2 2.45.57 3.57a1 1 0 0 1-.25 1z"/></symbol>
    <symbol id="i-mail" viewBox="0 0 24 24"><path d="M2 5h20v14H2z"/><path d="M2 5l10 8 10-8" fill="none" stroke="#fff" stroke-width="2"/></symbol>
    <symbol id="i-globe" viewBox="0 0 24 24"><path d="M12 2a10 10 0 1 0 0 20 10 10 0 0 0 0-20zm6.9 6h-2.9a15.6 15.6 0 0 0-1.4-3.6A8 8 0 0 1 18.9 8zM12 4c.8 1.2 1.5 2.5 1.9 4h-3.8c.4-1.5 1.1-2.8 1.9-4zM4.3 14a8 8 0 0 1 0-4h3.4a16 16 0 0 0 0 4zm.8 2h2.9a15.6 15.6 0 0 0 1.4 3.6A8 8 0 0 1 5.1 16zM8 8H5.1a8 8 0 0 1 4.3-3.6A15.6 15.6 0 0 0 8 8zm4 12c-.8-1.2-1.5-2.5-1.9-4h3.8c-.4 1.5-1.1 2.8-1.9 4zm2.3-6H9.7a14.6 14.6 0 0 1 0-4h4.6a14.6 14.6 0 0 1 0 4zm.3 5.6a15.6 15.6 0 0 0 1.4-3.6h2.9a8 8 0 0 1-4.3 3.6zM16.3 14a16 16 0 0 0 0-4h3.4a8 8 0 0 1 0 4z"/></symbol>
    <symbol id="i-pin" viewBox="0 0 24 24"><path d="M12 2a7 7 0 0 0-7 7c0 5.2 7 13 7 13s7-7.8 7-13a7 7 0 0 0-7-7zm0 9.5a2.5 2.5 0 1 1 0-5 2.5 2.5 0 0 1 0 5z"/></symbol>
  </defs>
</svg>

<section class="postcard postcard--front">
  <svg class="front-art" viewBox="0 0 695 463" aria-hidden="true">
    <defs>
      <linearGradient id="frontWash" x1="0" y1="0" x2="0" y2="1">
        <stop offset="0" stop-color="#dfe7f2"/>
        <stop offset="0.6" stop-color="#e6ebf2"/>
        <stop offset="1" stop-color="#ead8d0"/>
      </linearGradient>
      <linearGradient id="duskPhoto" x1="0" y1="0" x2="0" y2="1">
        <stop offset="0" stop-color="#5b86c6"/>
        <stop offset="0.35" stop-color="#a9b9d3"/>
        <stop offset="0.55" stop-color="#8a4a35"/>
        <stop offset="0.8" stop-color="#c8532a"/>
        <stop offset="1" stop-color="#d8692f"/>
      </linearGradient>
    </defs>
    <rect width="695" height="463" fill="url(#frontWash)"/>
    <polygon role="img" aria-label="Photo of a downtown street at dusk with tall office buildings and a lit street lamp" points="337,0 456,0 262,463 136,463" fill="url(#duskPhoto)"/>
    <polygon role="img" aria-label="Photo of a lit brick office entrance on a city street at dusk" points="479,0 695,0 695,190 620,463 290,463" fill="url(#duskPhoto)" opacity="0.9"/>
    <polygon points="456,0 479,0 290,463 262,463" fill="#f1f3f7" opacity="0.85"/>
    <rect x="470" y="0" width="225" height="140" fill="#e6ecf4" opacity="0.8"/>
  </svg>

  <h1 class="headline">
    <strong>MAXIMIZE YOUR</strong><br>
    <strong>FINANCIAL</strong><br>
    <strong>RETURNS</strong> with<br>
    support from<br>
    our rental<br>
    specialists
  </h1>

  <div class="brand brand--front">
    <span class="brand__name">BrightKey</span>
    <span class="brand__tag">Property Management</span>
  </div>
  <div class="front-rule"></div>
  <ul class="front-contact">
    <li><svg class="icon"><use href="#i-phone"/></svg>(806) 555-0147</li>
    <li><svg class="icon"><use href="#i-mail"/></svg>info@brightkeyrentals-example.com</li>
    <li><svg class="icon"><use href="#i-globe"/></svg>brightkeyrentals-example.com</li>
    <li><svg class="icon"><use href="#i-pin"/></svg>2287 Marble Lane, Lubbock, TX 79555</li>
  </ul>
</section>

<section class="postcard postcard--back">
  <svg class="back-art" viewBox="0 0 695 463" aria-hidden="true">
    <defs>
      <linearGradient id="backPhotoTone" x1="0" y1="0" x2="0" y2="1">
        <stop offset="0" stop-color="#0d4a8c"/>
        <stop offset="0.42" stop-color="#1f5799"/>
        <stop offset="0.5" stop-color="#8ea3c7"/>
        <stop offset="0.8" stop-color="#aeb5c6"/>
        <stop offset="1" stop-color="#b9b3b4"/>
      </linearGradient>
    </defs>
    <polygon role="img" aria-label="Photo of two agents meeting in an office above a city skyline at dusk" points="0,0 377,0 465,463 0,463" fill="url(#backPhotoTone)"/>
    <polygon points="377,0 383,0 489,463 465,463" fill="var(--navy-deep)"/>
  </svg>

  <div class="brand brand--back">
    <span class="brand__name">BrightKey</span>
    <span class="brand__tag">Property Management</span>
    <span class="brand__address">2287 Marble Lane, Lubbock, TX 79555</span>
  </div>

  <div class="services">
    <h2 class="services__title">DISCOVER<br>OUR SERVICES</h2>
    <div class="services__rule"></div>
    <ul class="services__list">
      <li><svg class="tick" viewBox="0 0 15 15"><rect width="15" height="15" rx="2" fill="var(--check)"/><path d="M3.5 7.8l2.6 2.6 5.4-5.6" fill="none" stroke="#fff" stroke-width="1.8"/></svg>Property Marketing</li>
      <li><svg class="tick" viewBox="0 0 15 15"><rect width="15" height="15" rx="2" fill="var(--check)"/><path d="M3.5 7.8l2.6 2.6 5.4-5.6" fill="none" stroke="#fff" stroke-width="1.8"/></svg>Tenant Screening</li>
      <li><svg class="tick" viewBox="0 0 15 15"><rect width="15" height="15" rx="2" fill="var(--check)"/><path d="M3.5 7.8l2.6 2.6 5.4-5.6" fill="none" stroke="#fff" stroke-width="1.8"/></svg>Rent Collection</li>
      <li><svg class="tick" viewBox="0 0 15 15"><rect width="15" height="15" rx="2" fill="var(--check)"/><path d="M3.5 7.8l2.6 2.6 5.4-5.6" fill="none" stroke="#fff" stroke-width="1.8"/></svg>Maintenance</li>
      <li><svg class="tick" viewBox="0 0 15 15"><rect width="15" height="15" rx="2" fill="var(--check)"/><path d="M3.5 7.8l2.6 2.6 5.4-5.6" fill="none" stroke="#fff" stroke-width="1.8"/></svg>Property Inspections</li>
      <li><svg class="tick" viewBox="0 0 15 15"><rect width="15" height="15" rx="2" fill="var(--check)"/><path d="M3.5 7.8l2.6 2.6 5.4-5.6" fill="none" stroke="#fff" stroke-width="1.8"/></svg>Financial Reporting</li>
      <li><svg class="tick" viewBox="0 0 15 15"><rect width="15" height="15" rx="2" fill="var(--check)"/><path d="M3.5 7.8l2.6 2.6 5.4-5.6" fill="none" stroke="#fff" stroke-width="1.8"/></svg>Evictions</li>
      <li><svg class="tick" viewBox="0 0 15 15"><rect width="15" height="15" rx="2" fill="var(--check)"/><path d="M3.5 7.8l2.6 2.6 5.4-5.6" fill="none" stroke="#fff" stroke-width="1.8"/></svg>Legal Guidance</li>
    </ul>
  </div>

  <div class="back-contact">
    <div class="back-contact__phone"><svg class="icon"><use href="#i-phone"/></svg>(806) 555-0147</div>
    <ul class="back-contact__lines">
      <li><svg class="icon"><use href="#i-mail"/></svg>info@brightkeyrentals-example.com</li>
      <li><svg class="icon"><use href="#i-globe"/></svg>brightkeyrentals-example.com</li>
    </ul>
  </div>
</section>

</body>
</html>
```